Redesign of the UI of a customer service platform

To improve the user experience of our customers, we need a new design for our agent interface of our customer service platform (lunorbit.com).
The focus will be on the dashboard and the inbox screens (see attached) along with the common UI elements (Buttons, menu, fonts, forms...)
We want a simple and distinctive design

Target Market(s)

Worldwide

Industry/Entity Type

It Service

Number of Pages Required

3 page

Font styles to use
Sans Serif

Requirements
Must have
• New Onboarding page: this is a new page that is shown to user the first time they login to the platform. This will replace the current onboarding screen (setup SMS, Setup widget...etc)
• Dashboard page: to access important information and activate services (see screenshot from current site)
• Inbox page: to manage all the interactions with customers. (see screenshot from current site)
• UI elements (buttons, menus, forms, tables, fonts, color palette)

```html
<!DOCTYPE html>
<html lang="en">
<head>
<meta charset="utf-8">
<title>Lunorbit – Get Started</title>
<link href="https://fonts.googleapis.com/css2?family=Raleway:wght@200;300;400;500&display=swap" rel="stylesheet">
<style>
:root{
  --bar:#363b40;
  --accent:#f26b4a;
  --side-text:#a3a8ad;
  --ink:#3e4247;
  --muted:#6b7075;
  --panel:#e8e8e8;
  --navy:#3f4e6b;
  --blue:#1a82e2;
  --green:#1e8f3c;
  --info-bg:#e9f3fc;
  --info:#2f7fd6;
  --online:#23b14d;
}
*{box-sizing:border-box;margin:0;padding:0}
html,body{width:1200px;height:674px;overflow:hidden}
body{font-family:"Raleway",sans-serif;background:#fff;color:var(--ink);position:relative}
.topbar{position:absolute;left:0;top:0;width:1200px;height:37px;background:var(--bar);border-bottom:3px solid var(--accent)}
.topbar *{position:absolute}
.menu-toggle{left:54px;top:11px}
.top-icon{top:10px}
.count{width:12px;height:12px;border-radius:50%;background:var(--accent);color:#fff;font-size:8px;line-height:12px;text-align:center;font-family:"Raleway",sans-serif}
.status-dot{left:889px;top:12px;width:12px;height:12px;border-radius:50%;background:var(--online)}
.top-label{color:#e6e8ea;font-size:11.5px;top:11px;letter-spacing:.3px}
.help{left:1153px;top:0;width:47px;height:37px;background:var(--accent)}
.help span{left:17px;top:13px;width:11px;height:11px;border-radius:50%;background:#fff;color:var(--accent);font-size:8px;font-weight:500;text-align:center;line-height:11px}
.sidebar{position:absolute;left:0;top:40px;width:129px;height:634px;background:var(--bar);border-right:3px solid var(--accent)}
.nav-item{position:absolute;left:0;width:126px;text-align:center;color:var(--side-text);font-size:11px}
.nav-item svg{display:block;margin:0 auto 4px}
.nav-badge{position:absolute;left:88px;width:20px;height:20px;border-radius:50%;background:#fff;color:var(--bar);font-size:12px;line-height:20px;text-align:center}
.notice{position:absolute;left:751px;top:43px;width:183px;height:25px;background:var(--info-bg);border:1px solid var(--info);border-radius:2px;color:var(--info);font-size:9.5px;display:flex;align-items:center;padding-left:10px;gap:8px}
.notice::before{content:"";position:absolute;left:14px;top:-6px;width:8px;height:8px;background:var(--info-bg);border-left:1px solid var(--info);border-top:1px solid var(--info);transform:rotate(45deg)}
.notice .i{width:13px;height:13px;border-radius:50%;background:var(--info);color:#fff;font-size:9px;text-align:center;line-height:13px;font-weight:500}
.notice .x{margin-left:4px;font-size:12px}
.goals{position:absolute;left:590px;top:68px;display:flex;align-items:center;gap:10px}
.goals-num{font-size:15px;color:var(--ink)}
.goals-label{font-size:7px;color:var(--muted);letter-spacing:.3px}
.player{position:absolute;left:388px;top:137px;width:551px;height:308px;background:var(--panel);border-radius:4px}
.player-title{position:absolute;left:0;width:100%;top:98px;text-align:center;font-weight:200;font-size:92px;color:#111;letter-spacing:1px;line-height:1}
.player-time{position:absolute;left:45px;top:286px;font-size:9px;color:var(--muted)}
.addons-title{position:absolute;left:0;width:1326px;top:474px;text-align:center;font-size:18px;font-weight:300;letter-spacing:1.5px;color:var(--ink)}
.addon{position:absolute;top:528px;width:140px;text-align:center;font-size:15px;line-height:18px;color:var(--ink)}
.addon .icon{height:64px;display:flex;justify-content:center;align-items:flex-start;margin-bottom:16px}
.dollar{font-size:74px;font-weight:200;color:var(--accent);line-height:60px}
</style>
</head>
<body>
<header class="topbar">
  <svg class="menu-toggle" width="17" height="14" viewBox="0 0 17 14"><g fill="#cfd2d5"><rect y="0" width="17" height="2"/><rect y="4" width="17" height="2"/><rect y="8" width="17" height="2"/><rect y="12" width="17" height="2"/></g></svg>
  <svg class="top-icon" style="left:759px" width="14" height="13" viewBox="0 0 14 13"><g fill="#fff"><rect width="2" height="2"/><rect x="4" width="10" height="2"/><rect y="4" width="2" height="2"/><rect x="4" y="4" width="10" height="2"/><rect y="8" width="2" height="2"/><rect x="4" y="8" width="10" height="2"/><rect y="11" width="2" height="2"/><rect x="4" y="11" width="10" height="2"/></g></svg>
  <span class="count" style="left:769px;top:21px">2</span>
  <svg class="top-icon" style="left:823px;top:12px" width="17" height="12" viewBox="0 0 17 12"><path fill="#fff" d="M3 0h11l3 6v6H0V6zM2 6h4l1 2h3l1-2h4L13 2H4z"/></svg>
  <span class="count" style="left:836px;top:21px">4</span>
  <span class="status-dot"></span>
  <span class="top-label" style="left:914px">Availability</span>
  <svg style="left:983px;top:15px" width="9" height="6" viewBox="0 0 9 6"><path d="M1 1l3.5 3.5L8 1" stroke="#e6e8ea" stroke-width="1.4" fill="none"/></svg>
  <svg style="left:1037px;top:6px" width="24" height="24" viewBox="0 0 24 24"><circle cx="12" cy="12" r="12" fill="#fff"/><circle cx="12" cy="9" r="4.5" fill="var(--bar)"/><path d="M4 20c2-5 14-5 16 0" fill="var(--bar)"/></svg>
  <span class="top-label" style="left:1073px">User 1</span>
  <svg style="left:1117px;top:15px" width="9" height="6" viewBox="0 0 9 6"><path d="M1 1l3.5 3.5L8 1" stroke="#e6e8ea" stroke-width="1.4" fill="none"/></svg>
  <div class="help"><span>?</span></div>
</header>

<nav class="sidebar">
  <div class="nav-item" style="top:18px"><svg width="24" height="22" viewBox="0 0 24 22"><circle cx="12" cy="9" r="8" fill="#a3a8ad"/><path d="M1 22c2-6 20-6 22 0z" fill="#a3a8ad"/></svg>Dashboard</div>
  <div class="nav-item" style="top:101px"><svg width="22" height="16" viewBox="0 0 17 12"><path fill="#a3a8ad" d="M3 0h11l3 6v6H0V6zM2 6h4l1 2h3l1-2h4L13 2H4z"/></svg>Inbox</div>
  <span class="nav-badge" style="top:90px">4</span>
  <div class="nav-item" style="top:180px"><svg width="16" height="15" viewBox="0 0 14 13"><g fill="#a3a8ad"><rect width="2" height="2"/><rect x="4" width="10" height="2"/><rect y="4" width="2" height="2"/><rect x="4" y="4" width="10" height="2"/><rect y="8" width="2" height="2"/><rect x="4" y="8" width="10" height="2"/><rect y="11" width="2" height="2"/><rect x="4" y="11" width="10" height="2"/></g></svg>Tasks</div>
  <span class="nav-badge" style="top:170px">2</span>
  <div class="nav-item" style="top:259px"><svg width="16" height="16" viewBox="0 0 16 16"><circle cx="8" cy="4.5" r="4" fill="#a3a8ad"/><path d="M0 16c0-7 16-7 16 0z" fill="#a3a8ad"/></svg>Customers</div>
  <div class="nav-item" style="top:339px"><svg width="17" height="16" viewBox="0 0 17 16"><path d="M0 0l17 8-17 8 2-8z" fill="#a3a8ad"/></svg>Campaigns</div>
  <div class="nav-item" style="top:417px"><svg width="12" height="18" viewBox="0 0 12 18"><text x="6" y="16" text-anchor="middle" font-size="19" font-family="Raleway,sans-serif" font-weight="500" fill="#a3a8ad">$</text></svg>Payments</div>
  <div class="nav-item" style="top:499px"><svg width="16" height="14" viewBox="0 0 16 14"><g fill="#a3a8ad"><rect y="5" width="2" height="9"/><rect x="4.5" y="2" width="2" height="12"/><rect x="9" y="0" width="2" height="14"/><rect x="13.5" y="4" width="2" height="10"/></g></svg>Reports</div>
  <div class="nav-item" style="top:578px"><svg width="16" height="16" viewBox="0 0 16 16"><circle cx="8" cy="8" r="5.5" fill="none" stroke="#a3a8ad" stroke-width="3" stroke-dasharray="2.6 1.7"/><circle cx="8" cy="8" r="3.2" fill="none" stroke="#a3a8ad" stroke-width="2"/></svg>Settings</div>
</nav>

<div class="notice"><span class="i">i</span>New task has been assigned.<span class="x">✕</span></div>

<div class="goals">
  <svg width="40" height="40" viewBox="0 0 40 40"><circle cx="20" cy="20" r="18" fill="none" stroke="#e5e5e5" stroke-width="2"/><circle cx="20" cy="20" r="18" fill="none" stroke="#f5a623" stroke-width="2" stroke-dasharray="84.8 113" transform="rotate(-90 20 20)"/><text x="20" y="23" text-anchor="middle" font-size="8.5" font-family="Raleway,sans-serif" fill="#3e4247">75%</text></svg>
  <div><div class="goals-num">15</div><div class="goals-label">GOALS COMPLETED</div></div>
</div>

<section class="player">
  <div class="player-title">Get Started</div>
  <svg style="position:absolute;left:24px;top:283px" width="14" height="15" viewBox="0 0 14 15"><path d="M0 0l14 7.5L0 15z" fill="#6d7e9e"/></svg>
  <span class="player-time">0:10</span>
  <svg style="position:absolute;left:76px;top:285px" width="428" height="8" viewBox="0 0 428 8"><defs><linearGradient id="prog" x1="0" x2="1"><stop offset="0" stop-color="#f5a623"/><stop offset="1" stop-color="#e63946"/></linearGradient></defs><rect y="3" width="428" height="2" fill="#c9ccd4"/><rect y="3" width="77" height="2" fill="url(#prog)"/><circle cx="77" cy="4" r="3.5" fill="#fff" stroke="#e63946" stroke-width="1.5"/></svg>
  <svg style="position:absolute;left:512px;top:282px" width="15" height="15" viewBox="0 0 15 15"><g fill="none" stroke="#6d7e9e" stroke-width="1.6"><path d="M1 5V1h4M10 1h4v4M14 10v4h-4M5 14H1v-4M1 1l4 4M14 1l-4 4M14 14l-4-4M1 14l4-4"/></g></svg>
</section>

<h2 class="addons-title">Select your Add-ons</h2>

<div class="addon" style="left:283px"><div class="icon"><svg width="56" height="62" viewBox="0 0 56 62"><rect x="2" y="2" width="52" height="44" fill="none" stroke="var(--navy)" stroke-width="5"/><rect x="24" y="46" width="8" height="9" fill="var(--navy)"/><rect x="0" y="53" width="56" height="8" rx="2" fill="var(--navy)"/></svg></div>Widgets</div>
<div class="addon" style="left:438px"><div class="icon"><svg width="60" height="60" viewBox="0 0 60 60"><circle cx="30" cy="30" r="30" fill="var(--blue)"/></svg></div>Parlo<br>Messenger</div>
<div class="addon" style="left:593px"><div class="icon"><svg width="68" height="62" viewBox="0 0 68 62"><path d="M6 0h56a6 6 0 0 1 6 6v36a6 6 0 0 1-6 6H18L0 62V6a6 6 0 0 1 6-6z" fill="var(--green)"/><g fill="#fff"><rect x="20" y="22" width="6" height="6"/><rect x="31" y="22" width="6" height="6"/><rect x="42" y="22" width="6" height="6"/></g></svg></div>SMS</div>
<div class="addon" style="left:748px"><div class="icon"><svg width="60" height="60" viewBox="0 0 60 60"><circle cx="30" cy="30" r="30" fill="var(--accent)"/></svg></div>Skyline Chat</div>
<div class="addon" style="left:903px"><div class="icon"><span class="dollar">$</span></div>Payment</div>
</body>
</html>
```